Pemberton Dialworks Business Card Design

Double Sided Business Card Design for a Locksmith company specializing in Safecracking, safe & vault service.

```html
<!DOCTYPE html>
<html lang="en">
<head>
<meta charset="UTF-8">
<title>Pemberton Dialworks Business Card</title>
<link href="https://fonts.googleapis.com/css2?family=Archivo:wght@400;700&display=swap" rel="stylesheet">
<style>
  :root {
    --backdrop: #d6d6d6;
    --card: #141414;
    --card-edge: #1e7d3c;
    --green: #22883f;
    --white: #f2f2f2;
    --light: #c9c9c9;
    --muted: #3a3a3a;
    --rule: #8a8a8a;
  }
  * { margin: 0; padding: 0; box-sizing: border-box; }
  html, body { width: 1200px; height: 800px; overflow: hidden; }
  body {
    background: var(--backdrop);
    font-family: "Archivo", Arial, sans-serif;
    display: flex;
    align-items: center;
    justify-content: center;
    gap: 40px;
  }
  .card {
    width: 540px;
    height: 309px;
    background: var(--card);
    border-bottom: 3px solid var(--card-edge);
    position: relative;
    box-shadow: 0 10px 28px rgba(0,0,0,0.28);
  }

  /* Front side */
  .front .brand {
    position: absolute;
    left: 36px;
    top: 50%;
    transform: translateY(-50%);
    display: flex;
    align-items: center;
    gap: 12px;
  }
  .brand-dot {
    width: 34px; height: 34px;
    border-radius: 50%;
    background: var(--green);
    flex: none;
  }
  .front .brand-name {
    font-weight: 700;
    font-size: 21px;
    line-height: 1.05;
    letter-spacing: 0.5px;
    text-transform: uppercase;
    color: var(--white);
  }
  .front .divider {
    position: absolute;
    left: 300px;
    top: 62px;
    bottom: 62px;
    width: 1px;
    background: var(--rule);
  }
  .front .contact {
    position: absolute;
    left: 322px;
    top: 58px;
    color: var(--light);
    font-size: 11.5px;
    line-height: 1.45;
  }
  .contact .person-name {
    color: var(--green);
    font-weight: 700;
    font-size: 15px;
    letter-spacing: 0.4px;
    text-transform: uppercase;
  }
  .contact .person-title { margin-bottom: 12px; }
  .contact .address { margin-bottom: 12px; }
  .contact ul { list-style: none; }
  .contact li { display: flex; align-items: center; gap: 7px; }
  .contact svg { width: 10px; height: 10px; flex: none; }

  /* Back side */
  .back .brand {
    position: absolute;
    left: 0; right: 0;
    top: 96px;
    display: flex;
    align-items: center;
    justify-content: center;
    gap: 14px;
  }
  .back .brand-dot { width: 44px; height: 44px; background: #8f8f8f; }
  .back .brand-name {
    font-weight: 700;
    font-size: 27px;
    line-height: 1.05;
    letter-spacing: 0.6px;
    text-transform: uppercase;
    color: #6a6a6a;
  }
  .back .tagline {
    position: absolute;
    left: 0; right: 0;
    bottom: 52px;
    text-align: center;
    font-size: 12px;
    letter-spacing: 0.8px;
    color: var(--white);
    text-transform: uppercase;
  }
  .tagline .accent { color: var(--green); }
</style>
</head>
<body>
  <section class="card front">
    <div class="brand">
      <span class="brand-dot"></span>
      <span class="brand-name">Pemberton<br>Dialworks</span>
    </div>
    <div class="divider"></div>
    <div class="contact">
      <p class="person-name">Daniel Hartwell</p>
      <p class="person-title">President</p>
      <p class="address">4120 Larkspur Court<br>Bend, Oregon 97701</p>
      <ul>
        <li>
          <svg viewBox="0 0 10 10"><path d="M2 1l2 2-1 1.2c.6 1.2 1.6 2.2 2.8 2.8L7 6l2 2-1.3 1.3C4.5 9 1 5.5.7 2.3z" fill="var(--green)"/></svg>
          555-214-0187
        </li>
        <li>
          <svg viewBox="0 0 10 10"><rect x="2.5" y="0.5" width="5" height="9" rx="1" fill="none" stroke="var(--green)"/></svg>
          555-308-6642
        </li>
        <li>
          <svg viewBox="0 0 10 10"><rect x="1" y="4" width="8" height="5" fill="var(--green)"/><rect x="2.5" y="1" width="5" height="3" fill="none" stroke="var(--green)"/></svg>
          555-471-2093
        </li>
        <li>
          <svg viewBox="0 0 10 10"><rect x="0.5" y="2" width="9" height="6" fill="var(--green)"/><path d="M0.5 2l4.5 3.5L9.5 2" fill="none" stroke="var(--card)"/></svg>
          info@pembertondialworks.com
        </li>
        <li>
          <svg viewBox="0 0 10 10"><circle cx="5" cy="5" r="4.3" fill="none" stroke="var(--green)"/><ellipse cx="5" cy="5" rx="1.8" ry="4.3" fill="none" stroke="var(--green)"/><path d="M.7 5h8.6" stroke="var(--green)"/></svg>
          www.pembertondialworks.com
        </li>
      </ul>
    </div>
  </section>

  <section class="card back">
    <div class="brand">
      <span class="brand-dot"></span>
      <span class="brand-name">Pemberton<br>Dialworks</span>
    </div>
    <p class="tagline">Specializing in safecracking, <span class="accent">safe &amp; vault service</span></p>
  </section>
</body>
</html>
```